Home Page

We provide a Customer Relationship Management (CRM) and Email Marketing solution to medium and small sized businesses with sales teams from 10 to 500 sales people.

Our solution is cloud based and fully supported.

Our solution is unique in that:

1) Email marketing and CRM are in the same system - no transferring data back and forth - sales benefits directly and instantaneously from email analytics and marketing can segment and target messages based on sales intelligence and status.

2) Through our partnership with ProspectHeron.net, each user of our solution gets 500 business contacts they select with email addresses, every month!

3) Our solution is easy to tailor to each unique business and our team gets involved with every new client to help them customize our solution around their unique way of doing business.

So, our solution helps businesses reach more potential customers, close them and keep them.

With 500 potential customers you select each month, our solution lets you nurture them as they move through the sales process via email and afterward, as well as track and manage sales activity, history and pipeline.

Target Market(s)

CEOs, VP of Sales, Marketing Managers

Industry/Entity Type

Marketing

Requirements
Must have
• Trust symbols - QTR
Customer logos - Varn Telecom, QTR, Trellin Savings Union
Feature customer video - http://www.clipvault-example.com/watch?feature=player_embedded&v=ZQTrmwLpX4d
Graphical representation of our unique proposition - CRM + Email + Leads + Help to Get it working for you
Strong call to action - Start a 30 day free trial

```html
<!DOCTYPE html>
<html lang="en">
<head>
<meta charset="utf-8">
<title>Pipewren – Online CRM and Email Marketing</title>
<link href="https://fonts.googleapis.com/css2?family=Source+Sans+3:wght@400;600;700&display=swap" rel="stylesheet">
<style>
:root{
  --slate:#5e6367;
  --page:#ebebeb;
  --white:#ffffff;
  --orange:#e8502a;
  --red:#d9361b;
  --ink:#444444;
  --text:#6a6a6a;
  --heading:#666666;
  --nav:#444444;
  --border:#d6d6d6;
  --dark-btn:#3a3a3a;
  --footer-link:#b4b8bb;
  --trust:#1b5e9c;
}
*{margin:0;padding:0;box-sizing:border-box}
html,body{width:1116px;height:1200px;overflow:hidden}
body{font-family:"Source Sans 3",sans-serif;background:var(--page);position:relative;color:var(--text)}
.top-band{position:absolute;left:0;top:0;width:1116px;height:378px;background:var(--slate)}
.header{position:absolute;left:92px;top:0;width:930px;height:116px;background:linear-gradient(#f1f1f1,#fdfdfd);box-shadow:0 0 18px rgba(0,0,0,.35)}
.brand{position:absolute;left:53px;top:22px}
.brand-name{font-size:50px;font-weight:700;color:var(--orange);letter-spacing:-1.5px;line-height:1}
.brand-tag{display:flex;align-items:center;gap:5px;margin-top:4px;font-size:13.5px;font-weight:700;color:var(--ink);letter-spacing:.2px}
.nav{position:absolute;left:92px;top:116px;width:930px;height:38px;background:linear-gradient(#3e3e3e,#555555);display:flex;align-items:center;padding-left:57px}
.nav a{color:var(--white);text-decoration:none;font-size:15px;padding:0 22px;border-left:1px solid #6a6a6a;line-height:16px}
.nav a:first-child{border-left:none;padding-left:0}
.hero{position:absolute;left:92px;top:154px;width:930px;height:224px;background:linear-gradient(90deg,#d4eaf0 0%,#e3f2f5 55%,#eef5f6 100%);overflow:hidden}
.hero-photo{position:absolute;right:0;top:0;width:360px;height:224px;background:radial-gradient(ellipse at 65% 45%,#e7c4ad 0%,#d8c8c0 30%,#e9eef0 70%,#eef4f5 100%)}
.welcome{position:absolute;left:108px;top:29px;width:430px;height:150px;background:rgba(200,225,230,.55);padding:20px 24px}
.welcome h1{font-size:14px;font-weight:700;color:var(--ink)}
.welcome h1 span,.welcome p b{color:var(--orange)}
.welcome p{margin-top:12px;font-size:13.5px;line-height:16.5px;color:var(--text);width:380px}
.btn-red{position:absolute;background:var(--red);color:var(--white);font-weight:700;font-size:14.5px;text-align:center;line-height:22px}
.hero .btn-red{left:425px;top:189px;width:113px;height:22px}
.feature{position:absolute;top:395px;width:209px}
.feature .head{height:70px;display:flex;align-items:center;gap:12px;padding-left:18px}
.feature .icon{width:61px;height:61px;border-radius:50%;background:var(--orange);display:flex;align-items:center;justify-content:center;flex:none}
.feature h2{font-size:17.5px;font-weight:700;color:var(--heading);line-height:20px}
.feature .card{margin-top:6px;height:160px;background:var(--white);border:1px solid var(--border);padding:22px 16px 0 18px;font-size:13.5px;line-height:16.3px;position:relative}
.feature .card b{color:var(--ink);font-weight:600}
.btn-dark{position:absolute;left:57px;bottom:22px;width:92px;height:22px;background:var(--dark-btn);color:var(--white);font-weight:700;font-size:14px;text-align:center;line-height:22px}
.signup{position:absolute;left:767px;top:395px;width:255px;height:236px;background:var(--white)}
.signup h2{text-align:center;margin-top:22px;font-size:17.5px;line-height:21px;font-weight:700;color:var(--heading)}
.signup h2 span{color:var(--orange);display:block}
.field{position:absolute;left:22px;width:203px;height:25px;border:1px solid var(--border);font-size:14.5px;color:var(--ink);padding:3px 11px}
.signup .btn-red{left:132px;top:178px;width:92px;height:22px}
.about{position:absolute;left:108px;top:703px;width:405px;font-size:14.5px;line-height:17.5px}
.about p+p{margin-top:17px}
.about .watch{display:block;margin-top:19px;color:var(--orange);font-weight:700;font-size:13.5px;text-decoration:none}
.video{position:absolute;left:590px;top:676px;width:432px;height:255px;background:var(--white)}
.video .vlogo{position:absolute;left:0;width:432px;top:85px;text-align:center;font-size:50px;font-weight:700;color:var(--orange);letter-spacing:-1.5px}
.video .caption{position:absolute;left:0;top:207px;width:432px;height:26px;background:#f04e1c;font-family:"Times New Roman",serif;color:#1a1a1a;font-size:13px;padding:7px 8px 0}
.video .controls{position:absolute;left:0;top:233px;width:432px;height:22px;background:#1b1b1b}
.progress{position:absolute;left:0;top:0;width:432px;height:4px;background:#444}
.progress i{position:absolute;left:0;top:0;width:95px;height:4px;background:#888}
.time{position:absolute;left:61px;top:9px;font-size:7px;color:#ddd;font-family:Arial,sans-serif}
.clients{position:absolute;top:1040px;left:130px;display:flex;align-items:center;gap:26px;font-weight:700}
.client-varn{font-size:22px;color:#3a8fc0}
.client-trellin{font-size:22px;color:var(--trust)}
.trust-badge{position:absolute;left:941px;top:1025px;width:39px;height:50px;background:var(--trust)}
.footer{position:absolute;left:0;top:1086px;width:1116px;height:114px;background:var(--slate)}
.footer nav{position:absolute;left:128px;top:13px;font-size:15px;color:var(--footer-link)}
.footer nav a{color:var(--footer-link);text-decoration:none}
.footer nav .sep{margin:0 6px}
.copyright{position:absolute;right:136px;top:17px;font-size:12px;color:#c9cccf}
</style>
</head>
<body>
<div class="top-band"></div>

<header class="header">
  <div class="brand">
    <div class="brand-name">pipewren</div>
    <div class="brand-tag">
      <svg width="10" height="13" viewBox="0 0 10 13"><path d="M1 1l6 5.5L1 12" fill="none" stroke="#e8502a" stroke-width="3"/></svg>
      ONLINE CRM AND EMAIL MARKETING.
    </div>
  </div>
</header>

<nav class="nav">
  <a href="#">Home</a><a href="#">About Us</a><a href="#">Privacy Policy</a><a href="#">Terms and conditions</a><a href="#">Contact Us</a>
</nav>

<section class="hero">
  <div class="hero-photo" role="img" aria-label="Photo of a smiling customer support agent wearing a headset, with colleagues in soft focus behind"></div>
  <div class="welcome">
    <h1>WELCOME TO <span>pipewren</span></h1>
    <p>At <b>pipewren</b> lorem ipsum dolor sit amet, consectetur adipisicing elit, sed do eiusmod tempor incididunt ut labore et dolore magna aliqua.</p>
  </div>
  <a class="btn-red">Find out more</a>
</section>

<div class="feature" style="left:92px">
  <div class="head">
    <div class="icon"><svg width="30" height="22" viewBox="0 0 30 22"><rect x="1" y="1" width="28" height="20" fill="none" stroke="#fff" stroke-width="2"/><path d="M1 1l14 11L29 1M1 21l10-9M29 21l-10-9" fill="none" stroke="#fff" stroke-width="2"/></svg></div>
    <h2>CRM<br>+ Email</h2>
  </div>
  <div class="card"><b>No transferring data back and forth</b> - sales benefits directly and instantaneously from email analytics and marketing<a class="btn-dark">Learn More</a></div>
</div>

<div class="feature" style="left:315px">
  <div class="head">
    <div class="icon"><svg width="34" height="28" viewBox="0 0 34 28"><path d="M3 7l7 8 7-12 7 12 7-8-2 18H5z" fill="none" stroke="#fff" stroke-width="2.5" stroke-linejoin="round"/></svg></div>
    <h2>Leads</h2>
  </div>
  <div class="card">Each user of our solution gets <b>500 business contacts</b> they select with email addresses, every month!<a class="btn-dark">Learn More</a></div>
</div>

<div class="feature" style="left:538px">
  <div class="head">
    <div class="icon"><svg width="32" height="30" viewBox="0 0 32 30"><rect x="2" y="6" width="22" height="22" fill="none" stroke="#fff" stroke-width="2.5"/><path d="M8 15l5 6L29 2" fill="none" stroke="#fff" stroke-width="4"/></svg></div>
    <h2>Help to Get<br>it working</h2>
  </div>
  <div class="card">Our solution is <b>easy to tailor</b> to each unique business and our team gets involved with every new client to help them customize our solution<a class="btn-dark">Learn More</a></div>
</div>

<aside class="signup">
  <h2>Get started Now<span>30 day free trial</span></h2>
  <div class="field" style="top:90px">Name|</div>
  <div class="field" style="top:128px">E-mail Adress|</div>
  <a class="btn-red">Sign Up</a>
</aside>

<section class="about">
  <p>Lorem ipsum dolor sit amet, consectetur adipisicing elit, sed do eiusmod tempor incididunt ut labore et dolore magna aliqua.</p>
  <p>Ut enim ad minim veniam, quis nostrud exercitation ullamco laboris nisi ut aliquip ex ea commodo consequat. Duis aute irure dolor in reprehenderit in voluptate velit esse cillum dolore eu fugiat nulla pariatur. Excepteur sint occaecat cupidatat non proident, sunt in culpa qui officia deserunt mollit anim id est.</p>
  <a class="watch" href="http://www.clipvault-example.com/watch?feature=player_embedded&amp;v=ZQTrmwLpX4d">Watch The video to learn more &gt;&gt;</a>
</section>

<div class="video">
  <div class="vlogo">pipewren</div>
  <div class="caption">Sales CRM, Email Marketing and Sales Leads, all in one easy to use solution!</div>
  <div class="controls">
    <div class="progress"><i></i></div>
    <svg style="position:absolute;left:15px;top:9px" width="10" height="10" viewBox="0 0 10 10"><path d="M1 0l8 5-8 5z" fill="#aaa"/></svg>
    <svg style="position:absolute;left:40px;top:9px" width="12" height="10" viewBox="0 0 12 10"><path d="M0 3h3l4-3v10L3 7H0z" fill="#aaa"/></svg>
    <span class="time">0:03 / 2:02</span>
    <svg style="position:absolute;right:10px;top:8px" width="100" height="11" viewBox="0 0 100 11"><rect x="0" y="3" width="9" height="5" fill="#aaa"/><circle cx="25" cy="5.5" r="4" fill="#aaa"/><circle cx="45" cy="5.5" r="3.5" fill="#aaa"/><rect x="59" y="2" width="11" height="7" fill="none" stroke="#fff" stroke-width="1.5"/><rect x="78" y="2" width="11" height="7" fill="none" stroke="#aaa" stroke-width="1.2"/><path d="M93 1h3M93 1v3M100 1h-3M100 1v3M93 10h3M93 10v-3M100 10h-3M100 10v-3" stroke="#aaa" stroke-width="1.2"/></svg>
  </div>
</div>

<div class="clients">
  <span class="client-varn">Varn Telecom</span>
  <span class="client-trellin">Trellin Savings Union</span>
</div>
<div class="trust-badge" role="img" aria-label="QTR trust badge"></div>

<footer class="footer">
  <nav>
    <a href="#">home</a><span class="sep">|</span><a href="#">about us</a><span class="sep">|</span><a href="#">privacy policy</a><span class="sep">|</span><a href="#">terms and conditions</a><span class="sep">|</span><a href="#">contact us</a>
  </nav>
  <div class="copyright">© Copyright pipewren. - All rights reserved</div>
</footer>
</body>
</html>
```